International Trading Company, 'KIRO' needs a Business Card

The company name is "KIRO" and it has own logo design.
I'd like to use its logo on this business card.
I need two side Business Card.
I'll look forward to your great design.
Thank you very much in advance.

Contact Information for Business Card

Company Name : Kiro Harbour Limited
Information Example
Dorian Pallister
Mobile(use icon please) : 1 (212) 555-0143
Tel(use icon please) : 1 (212) 555-0178
Email(use icon please) : dorian27@kiroharbour-mail.com
Address(use icon please) : 482 Halden Ave, New York, NY 10160, USA

```html
<!DOCTYPE html>
<html lang="en">
<head>
<meta charset="utf-8">
<title>KIRO Business Card</title>
<link rel="stylesheet" href="https://fonts.googleapis.com/css2?family=Open+Sans:wght@300;400;600;700;800&display=swap">
<style>
  :root {
    --page-bg: #e9e9e9;
    --card-dark-top: #5e5e5e;
    --card-dark-bottom: #3c3c3c;
    --card-light: #f7f7f7;
    --ink-dark: #464646;
    --ink-mid: #5a5a5a;
    --ink-soft: #7a7a7a;
    --band-dark: #4b4b4b;
    --band-mid: #8a8a8a;
    --white: #ffffff;
  }
  * { margin: 0; padding: 0; box-sizing: border-box; }
  html, body { width: 1200px; height: 900px; overflow: hidden; }
  body {
    background: var(--page-bg);
    font-family: "Open Sans", Arial, sans-serif;
    display: flex;
    flex-direction: column;
    align-items: center;
    justify-content: center;
    gap: 30px;
  }
  .card {
    position: relative;
    width: 700px;
    height: 400px;
    overflow: hidden;
    box-shadow: 0 6px 18px rgba(0,0,0,0.18);
  }
  .card-front {
    background: linear-gradient(160deg, var(--card-dark-top), var(--card-dark-bottom));
    display: flex;
    align-items: center;
    justify-content: center;
  }
  .wordmark {
    font-weight: 800;
    letter-spacing: 4px;
    line-height: 1;
  }
  .card-front .wordmark { color: var(--white); font-size: 118px; }
  .card-back { background: var(--card-light); }
  .identity {
    position: absolute;
    left: 48px;
    top: 150px;
  }
  .card-back .wordmark { color: var(--ink-dark); font-size: 92px; }
  .person-name {
    margin-top: 14px;
    font-weight: 700;
    font-size: 21px;
    color: var(--ink-mid);
    letter-spacing: 0.3px;
  }
  .person-role {
    font-weight: 400;
    font-size: 19px;
    color: var(--ink-soft);
  }
  .contact-list {
    position: absolute;
    right: 34px;
    top: 62px;
    list-style: none;
    text-align: right;
    color: var(--ink-mid);
    font-size: 15.5px;
    line-height: 1.45;
  }
  .contact-list li {
    display: flex;
    justify-content: flex-end;
    align-items: flex-start;
    gap: 10px;
  }
  .contact-list .gap-above { margin-top: 12px; }
  .contact-icon { width: 14px; height: 14px; margin-top: 4px; flex: none; fill: var(--ink-mid); }
  .contact-icon.blank { visibility: hidden; }
  .footer-bands { position: absolute; left: 0; bottom: 0; width: 700px; height: 110px; }
  .website {
    position: absolute;
    right: 34px;
    bottom: 48px;
    color: var(--white);
    font-size: 14px;
    font-weight: 600;
    letter-spacing: 2.6px;
    white-space: nowrap;
  }
</style>
</head>
<body>

  <section class="card card-front" aria-label="Card front">
    <div class="wordmark">KIRO</div>
  </section>

  <section class="card card-back" aria-label="Card back">
    <div class="identity">
      <div class="wordmark">KIRO</div>
      <p class="person-name">DORIAN PALLISTER</p>
      <p class="person-role">CEO/FOUNDER</p>
    </div>

    <ul class="contact-list">
      <li>482 Halden Ave, New York
        <svg class="contact-icon" viewBox="0 0 24 24"><path d="M12 2a7 7 0 0 0-7 7c0 5 7 13 7 13s7-8 7-13a7 7 0 0 0-7-7zm0 9.5A2.5 2.5 0 1 1 12 6.5a2.5 2.5 0 0 1 0 5z"/></svg>
      </li>
      <li>NY 10160, USA
        <svg class="contact-icon blank" viewBox="0 0 24 24"></svg>
      </li>
      <li class="gap-above">1 (212) 555-0178
        <svg class="contact-icon" viewBox="0 0 24 24"><path d="M6.6 10.8a15 15 0 0 0 6.6 6.6l2.2-2.2a1 1 0 0 1 1-.25 11.4 11.4 0 0 0 3.6.57 1 1 0 0 1 1 1V20a1 1 0 0 1-1 1A17 17 0 0 1 3 4a1 1 0 0 1 1-1h3.5a1 1 0 0 1 1 1c0 1.25.2 2.45.57 3.57a1 1 0 0 1-.25 1z"/></svg>
      </li>
      <li>1 (212) 555-0143
        <svg class="contact-icon" viewBox="0 0 24 24"><path d="M7 1h10a2 2 0 0 1 2 2v18a2 2 0 0 1-2 2H7a2 2 0 0 1-2-2V3a2 2 0 0 1 2-2zm0 3v14h10V4zm5 15.5a1 1 0 1 0 0 2 1 1 0 0 0 0-2z"/></svg>
      </li>
      <li>dorian27@kiroharbour-mail.com
        <svg class="contact-icon" viewBox="0 0 24 24"><path d="M2 5h20v14H2zm2 2v.5l8 5 8-5V7zm0 2.8V17h16V9.8l-8 5z"/></svg>
      </li>
    </ul>

    <svg class="footer-bands" viewBox="0 0 700 110" preserveAspectRatio="none" aria-hidden="true">
      <polygon points="0,92 700,86 700,110 0,110" fill="var(--band-mid)"/>
      <polygon points="350,30 700,24 700,88 332,93" fill="var(--band-dark)"/>
    </svg>
    <p class="website">www.kiroharbour-mail.com</p>
  </section>

</body>
</html>
```